Home page web design for "Tales from Tamsin"

We need a home page web design for a start up company that will write memoirs for seniors.
The completed project will need to include PSD files...NO HTML or CSS necessary.
Attached is a brief outline concept that may give you some ideas...but you are the creative professionals, so please feel free to add your ideas. We will also attach some files that show you our logo, brochures, and photos that could be used to give you ideas of our focus.
There will need to be access to the other pages on the home page to include: 'About Us'; 'How We Can Help'; 'Community Sessions'; 'Senior Consulting ' and 'Contact Us'.
Updates

Project Deadline Extended Reason: We want designers to have sufficient time to get all their proposals and revisions submitted. THANK YOU Added Wednesday, October 15, 2014

Target Market(s)

Seniors and Baby Boomers

Industry/Entity Type

It Company

Number of Pages Required

1 page

Colors
f9ba93
fbca95
faa54b
faf289
f37123

Requirements
Must have
• Script easy on senior eyes.
• Initial contact number would be 844-4LEGACY
Nice to have
• While the color pallet is non-specific we prefer the warm colors.
• salmon, peach.......
• NOT so much the orange of Halloween:)
• However, please utilize your creativity and put in colors you feel will draw best with your design.

```html
<!DOCTYPE html>
<html lang="en">
<head>
<meta charset="utf-8">
<title>Tales from Tamsin — Home</title>
<link href="https://fonts.googleapis.com/css2?family=Alegreya:wght@400;700&family=Alegreya+Sans:wght@700&family=Cormorant+Garamond:ital,wght@1,600&family=Arimo:wght@400;700&display=swap" rel="stylesheet">
<style>
  :root {
    --salmon: #fb9f80;
    --salmon-light: #fdb89a;
    --peach: #fbca95;
    --orange: #f37123;
    --amber: #faa54b;
    --butter: #f2d06c;
    --ink: #2b2b2b;
    --script-ink: #2a1a14;
    --maroon: #6b0f12;
    --text: #333333;
    --white: #ffffff;
  }
  * { margin: 0; padding: 0; box-sizing: border-box; }
  html, body { width: 1145px; height: 1200px; overflow: hidden; background: var(--white); }
  .page { position: relative; width: 1145px; height: 1200px; font-family: "Arimo", Arial, sans-serif; color: var(--text); }

  .masthead {
    position: absolute; left: 0; top: 0; width: 1145px; height: 458px;
    background: radial-gradient(ellipse at 50% 45%, var(--salmon-light) 0%, var(--salmon) 60%);
  }
  .oval-photo {
    position: absolute; border-radius: 50%;
    box-shadow: 0 0 0 4px rgba(255, 230, 190, 0.85), 0 0 14px rgba(255, 220, 160, 0.9);
  }
  .oval-photo--sunset { left: 60px; top: 26px; width: 266px; height: 370px;
    background: linear-gradient(180deg, #f3dc7a 0%, #f0b54a 45%, #b3561c 70%, #2a130b 100%); }
  .oval-photo--writer { left: 814px; top: 26px; width: 248px; height: 366px;
    background: linear-gradient(160deg, #6a3b1e 0%, #3a1f10 45%, #b79c8a 75%, #5a3522 100%); }

  .script { font-family: "Cormorant Garamond", Georgia, serif; font-style: italic; font-weight: 600; color: var(--script-ink); }
  .site-url { position: absolute; left: 0; width: 1145px; top: 18px; text-align: center; font-size: 42px; line-height: 52px; letter-spacing: 1px; }
  .phones { position: absolute; left: 0; width: 1145px; top: 66px; text-align: center; font-size: 30px; line-height: 36px; letter-spacing: 0.5px; }
  .phones span { display: inline-flex; align-items: center; gap: 8px; margin: 0 10px; }
  .phones svg { width: 18px; height: 16px; }

  .brand-name {
    position: absolute; left: 0; width: 1145px; top: 200px; text-align: center;
    font-family: "Alegreya", serif; font-weight: 700; font-size: 52px; color: #8a3a14;
  }
  .brand-rule { position: absolute; left: 388px; top: 378px; width: 380px; height: 2px; background: rgba(140, 70, 40, 0.45); }

  .tagline { position: absolute; }
  .tagline--left { left: 48px; top: 404px; font-size: 28px; line-height: 32px; }
  .tagline--right { left: 764px; top: 402px; width: 330px; text-align: center; font-size: 23px; line-height: 20px; }

  .main-nav {
    position: absolute; left: 0; top: 458px; width: 1145px; height: 52px;
    background: linear-gradient(180deg, #f0b866 0%, #e59845 100%);
  }
  .main-nav ul { list-style: none; display: flex; position: absolute; left: 130px; top: 0; height: 52px; }
  .main-nav li a {
    display: block; height: 52px; line-height: 52px; padding: 0 13px;
    font-family: "Alegreya", serif; font-size: 17px; color: var(--white); text-decoration: none; letter-spacing: 0.3px;
  }
  .main-nav li.is-current a { background: var(--butter); color: var(--ink); font-weight: 700; }

  .content { position: absolute; left: 130px; top: 530px; width: 882px; text-align: center; }
  .welcome {
    font-family: "Alegreya Sans", sans-serif; font-size: 30px; color: var(--ink);
    display: flex; justify-content: center; align-items: center; gap: 22px; height: 56px;
  }
  .welcome em { font-style: normal; color: var(--maroon); }
  .flourish { width: 40px; height: 2px; background: #8a8a8a; }
  .dashed-rule { border-top: 1px dashed #c8c8c8; margin-top: 4px; }
  .lead { font-weight: 700; font-size: 23px; color: var(--ink); margin-top: 22px; }
  .intro { font-size: 19px; line-height: 28px; margin: 14px 30px 0; }
  .dotted-rule { border-top: 2px dotted #666; margin-top: 26px; }
  .body-copy { position: relative; }
  .body-copy p { font-size: 19px; line-height: 28px; margin-top: 14px; position: relative; }
  .body-copy p:first-child { margin-top: 28px; }
  .faint-photo {
    position: absolute; left: 250px; top: 40px; width: 380px; height: 230px; border-radius: 30px;
    background: radial-gradient(ellipse, rgba(210, 150, 130, 0.22) 0%, rgba(255, 255, 255, 0) 70%);
  }

  .cta-row { position: absolute; left: 131px; top: 1066px; width: 881px; height: 80px; }
  .gift-badge {
    position: absolute; left: 0; top: 6px; width: 86px; height: 66px; border-radius: 8px;
    background: linear-gradient(180deg, #f28a3a 0%, #c94a12 100%);
    display: flex; align-items: center; justify-content: center;
  }
  .cta-text { position: absolute; left: 105px; width: 545px; top: 0; font-size: 19px; line-height: 28px; text-align: center; }
  .learn-more {
    position: absolute; right: 0; top: 6px; width: 209px; height: 68px; border-radius: 8px;
    background: linear-gradient(180deg, #f7953f 0%, #c84a10 100%);
    display: flex; align-items: center; gap: 8px; padding-left: 16px;
    color: var(--white); font-weight: 700; font-size: 19px; text-decoration: none; white-space: nowrap;
  }
  .learn-more svg { flex: none; }

  .site-footer {
    position: absolute; left: 0; top: 1156px; width: 1145px; height: 44px;
    background: linear-gradient(180deg, #e89a4a 0%, #f2bf6a 100%);
    text-align: center; line-height: 44px; color: var(--white); font-size: 15px;
  }
</style>
</head>
<body>
<div class="page">
  <header class="masthead">
    <div class="oval-photo oval-photo--sunset" role="img" aria-label="Photo of an elderly couple walking by the water at sunset"></div>
    <div class="oval-photo oval-photo--writer" role="img" aria-label="Photo of an elderly woman writing at a wooden desk"></div>

    <p class="site-url script">www.talesfromtamsin.example</p>
    <p class="phones script">
      <span><svg viewBox="0 0 18 16"><ellipse cx="9" cy="7" rx="8" ry="6" fill="#2a1a14"/><path d="M5 11 L3 16 L9 12 Z" fill="#2a1a14"/></svg>717-555-0142</span>
      <span><svg viewBox="0 0 18 16"><ellipse cx="9" cy="7" rx="8" ry="6" fill="#2a1a14"/><path d="M5 11 L3 16 L9 12 Z" fill="#2a1a14"/></svg>844-555-0178</span>
    </p>

    <p class="brand-name">Tales from Tamsin</p>
    <div class="brand-rule"></div>

    <p class="tagline tagline--left script">When a genealogy doesn't say enough...</p>
    <p class="tagline tagline--right script">Every life legacy is a gift to be treasured by the next generation</p>
  </header>

  <nav class="main-nav">
    <ul>
      <li class="is-current"><a href="#">HOME</a></li>
      <li><a href="#">ABOUT US</a></li>
      <li><a href="#">HOW WE CAN HELP</a></li>
      <li><a href="#">COMMUNITY SESSIONS</a></li>
      <li><a href="#">SENIOR CONSULTING</a></li>
      <li><a href="#">CONTACT US</a></li>
    </ul>
  </nav>

  <main class="content">
    <h1 class="welcome"><span class="flourish"></span><span>WELCOME TO <em>TALES FROM TAMSIN</em></span><span class="flourish"></span></h1>
    <div class="dashed-rule"></div>
    <h2 class="lead">If you were alive in 100 years, what would you share with your descendants?</h2>
    <p class="intro">Now you have a vehicle to help you immortalize your thoughts for the future…specifically for those who will want to know!</p>
    <div class="dotted-rule"></div>

    <div class="body-copy">
      <div class="faint-photo" role="img" aria-label="Faint photo of a grandparent with a grandchild"></div>
      <p>We are not all presidents of countries or CEO’s of fortune 500 companies! But “<strong>every life legacy is a gift to be treasured by the next generation.</strong>”</p>
      <p>Does your family host generations of soldiers, doctors, farmers, scientists, mechanics, entrepreneurs, writers, politicians, contractors, pastors, artisans, athletes, musicians, etc..? Generational patterns can often emerge when writing your story that will interest the next generation.</p>
      <p>A genealogy, while very relevant, doesn’t offer the personal story of the names we find. A biography can place a deeper relevance on the face for future descendants. Every life is a legacy to pass forward and we at Tales from Tamsin believe everyone should chronicle their life journey in writing. This commitment allows you to be remembered for who you truly are as a person.</p>
    </div>
  </main>

  <section class="cta-row">
    <div class="gift-badge">
      <svg width="40" height="40" viewBox="0 0 40 40" aria-hidden="true">
        <rect x="4" y="12" width="32" height="8" fill="#fff"/>
        <rect x="7" y="22" width="26" height="16" fill="#fff"/>
        <rect x="18" y="12" width="4" height="26" fill="#d55a1a"/>
        <path d="M20 12 C12 2 6 8 14 12 Z M20 12 C28 2 34 8 26 12 Z" fill="none" stroke="#fff" stroke-width="2.5"/>
      </svg>
    </div>
    <p class="cta-text">Think about it….Do you know the triumphs and tribulations of your ancestors? Do you wish you did? Well, so will those falling into your personal family tree.</p>
    <a class="learn-more" href="#">
      <svg width="40" height="40" viewBox="0 0 44 44" aria-hidden="true">
        <rect x="12" y="2" width="28" height="14" rx="7" fill="none" stroke="#fff" stroke-width="2"/>
        <circle cx="10" cy="22" r="5" fill="#fff"/>
        <path d="M2 42 L2 34 Q10 26 18 34 L18 42 Z" fill="#fff"/>
      </svg>
      LEARN MORE
    </a>
  </section>

  <footer class="site-footer">© 2014 Tamsin. All Rights Reserved</footer>
</div>
</body>
</html>
```